SkyvoraQ Business Cards and Stationary Design

Need a design for our business cards and stationary. I want to carry on the theme of the logo. I want the business cards to have a design on the back. I would like the business cards and the stationary to carry the same theme, design scheme, and branding

Target Market(s)

Airlines and Maintenance Facilities

Industry/Entity Type

Aviation

Contact Information for Business Card

Name
Position Title
Address: 4827 Tollbeck Lane, Harwick Bay, Calverra, 34951
Office Number
Mobile Number
Email
Website

Font styles to use
Serif
Sans Serif

Colors

Designer to choose colors to be used in the design.

```html
<!DOCTYPE html>
<html lang="en">
<head>
<meta charset="utf-8">
<title>SkyvoraQ Business Card</title>
<link rel="stylesheet" href="https://fonts.googleapis.com/css2?family=Montserrat:wght@400;500;700&display=swap">
<style>
  :root {
    --backdrop: #d6d6d6;
    --card: #f7f7f7;
    --navy: #13285a;
    --sky: #2c7cc1;
    --ink: #4a4d52;
    --muted: #6b7077;
  }
  * { margin: 0; padding: 0; box-sizing: border-box; }
  html, body {
    width: 1200px;
    height: 835px;
    overflow: hidden;
    background: var(--backdrop);
    font-family: "Montserrat", Arial, sans-serif;
  }
  .canvas {
    width: 1200px;
    height: 835px;
    display: flex;
    align-items: center;
    justify-content: center;
    gap: 60px;
  }
  .card {
    width: 520px;
    height: 298px;
    background: var(--card);
    border-radius: 3px;
    box-shadow: 0 6px 18px rgba(0,0,0,0.12);
    position: relative;
  }
  .brand {
    position: absolute;
    top: 46px;
    left: 44px;
    display: flex;
    align-items: center;
    gap: 12px;
  }
  .brand-dot {
    width: 30px;
    height: 30px;
    border-radius: 50%;
    background: var(--sky);
  }
  .brand-name {
    font-weight: 700;
    font-size: 22px;
    letter-spacing: 3px;
    color: var(--navy);
    text-transform: uppercase;
  }
  .contact {
    position: absolute;
    left: 44px;
    bottom: 36px;
  }
  .person-name {
    font-weight: 700;
    font-size: 20px;
    letter-spacing: 1px;
    color: var(--navy);
    text-transform: uppercase;
  }
  .person-title {
    font-size: 11px;
    color: var(--muted);
    margin: 3px 0 10px;
  }
  .details {
    border-left: 2px solid var(--sky);
    padding-left: 10px;
    list-style: none;
  }
  .details li {
    font-size: 11.5px;
    line-height: 17px;
    color: var(--ink);
  }
  .card-back {
    display: flex;
    align-items: center;
    justify-content: center;
  }
  .back-mark {
    display: flex;
    flex-direction: column;
    align-items: center;
    gap: 16px;
  }
  .back-dot {
    width: 96px;
    height: 96px;
    border-radius: 50%;
    border: 9px solid var(--sky);
  }
  .back-name {
    font-weight: 700;
    font-size: 24px;
    letter-spacing: 4px;
    color: var(--navy);
    text-transform: uppercase;
  }
</style>
</head>
<body>
  <main class="canvas">
    <section class="card card-front">
      <div class="brand">
        <span class="brand-name">SkyvoraQ</span>
        <span class="brand-dot"></span>
      </div>
      <div class="contact">
        <h1 class="person-name">Daren Holloway</h1>
        <p class="person-title">Director Technical</p>
        <ul class="details">
          <li>M: 555 014 2276</li>
          <li>T: 555 014 2277</li>
          <li>Email: info@skyvoraq.com</li>
          <li>Web : www.skyvoraq.com</li>
          <li>Address: 4827 Tollbeck Lane</li>
          <li>Harwick Bay, Calverra, 34951</li>
        </ul>
      </div>
    </section>
    <section class="card card-back">
      <div class="back-mark">
        <span class="back-dot"></span>
        <span class="back-name">SkyvoraQ</span>
      </div>
    </section>
  </main>
</body>
</html>
```